make a fireworks website

we are manufacturer of fireworks in Asia.
we need a HD fireworks website for showing product to all world customers.
we also need an register for member system,location, forum,products..etc
I added my Logo for the company.
brightnova.com.hk

and please message me if you have
any question.
here some example of website:
http://www.skyplumeshow.com/
http://www.tornelupyro.com/
http://www.quarvel-pyro.co.uk/
http://www.mirethpyro.co.uk/

```html
<!DOCTYPE html>
<html lang="en">
<head>
<meta charset="utf-8">
<title>Brightnova – Fireworks Manufacturer</title>
<link href="https://fonts.googleapis.com/css2?family=PT+Sans:wght@400;700&family=PT+Sans+Narrow:wght@400;700&display=swap" rel="stylesheet">
<style>
:root{
  --purple:#5b2f86;
  --purple-deep:#4a2470;
  --ink:#333;
  --muted:#555;
  --line:#e0e0e0;
  --card-border:#dedede;
  --white:#fff;
  --slide-night:#2a0f3a;
  --slide-glow:#8a1f5a;
}
*{margin:0;padding:0;box-sizing:border-box}
html,body{width:950px;height:1200px;overflow:hidden;background:var(--white)}
body{position:relative;font-family:"PT Sans",Arial,sans-serif;color:var(--ink)}
a{color:inherit}

/* header */
.site-header{position:absolute;left:178px;top:0;width:595px;height:76px}
.brand{position:absolute;left:0;top:22px;display:flex;align-items:center;gap:7px}
.brand-dot{width:22px;height:22px;border-radius:50%;background:var(--purple)}
.brand-name{font-family:"PT Sans",Arial,sans-serif;font-weight:700;font-size:19px;color:var(--purple);letter-spacing:-.2px}
.main-nav{position:absolute;right:0;top:12px;height:64px;display:flex}
.main-nav a{display:flex;align-items:center;justify-content:center;height:45px;text-decoration:none;
  font-family:"PT Sans Narrow",Arial,sans-serif;font-weight:700;font-size:11px;color:#222;border-left:1px solid var(--line)}
.main-nav a:first-child{border-left:none}
.main-nav a.is-active{height:64px;padding-bottom:19px;background:linear-gradient(#fff,#ececec);border-bottom:2px solid var(--purple)}

/* slider */
.hero{position:absolute;left:178px;top:76px;width:595px;height:243px;overflow:hidden;
  background:radial-gradient(ellipse at 47% 35%,#d67a3a 0,#b2306a 18%,var(--slide-glow) 35%,var(--slide-night) 70%)}
.hero-arrow{position:absolute;top:94px;width:24px;height:24px;background:rgba(170,170,170,.75);display:flex;align-items:center;justify-content:center}
.hero-arrow.prev{left:0}.hero-arrow.next{right:0}
.hero-caption{position:absolute;left:0;bottom:0;width:100%;height:21px;background:rgba(0,0,0,.85);
  color:#fff;font-size:12.5px;line-height:21px;padding-left:14px}

/* welcome */
.section-title{position:absolute;left:178px;width:595px;text-align:center;font-family:"PT Sans Narrow",Arial,sans-serif;
  font-weight:700;font-size:20px;color:var(--purple)}
.welcome-title{top:337px}
.welcome-photo{position:absolute;left:178px;top:376px;width:120px;height:110px;
  background:radial-gradient(circle at 45% 35%,#f3e6f4 0,#c54b8e 22%,#53245c 50%,#150a1c 80%)}
.welcome-text{position:absolute;left:326px;top:377px;width:443px;font-size:7.8px;line-height:14px;color:var(--muted)}

/* products */
.products-title{top:516px}
.product-grid{position:absolute;left:178px;top:557px;width:595px;display:grid;grid-template-columns:repeat(3,190px);column-gap:12.5px;row-gap:11px}
.product-card{position:relative;height:145px;border:2px solid var(--card-border);background:#fff}
.product-photo{position:absolute;left:40px;top:6px;width:106px;height:100px;border-radius:4px}
.product-label{position:absolute;left:12px;top:110px;width:160px;height:22px;background:var(--purple);color:#fff;
  text-align:center;line-height:22px;font-family:"PT Sans Narrow",Arial,sans-serif;font-weight:700;font-size:12px}
.tone-fountain{background:linear-gradient(90deg,#5bb6e0,#e86cb0,#f3d64a,#4a6fd0)}
.tone-kit{background:linear-gradient(135deg,#3a3a4a,#c23a3a,#e0b040,#4a7fc0)}
.tone-rocket{background:linear-gradient(#6a6f80,#9aa0b0 60%,#c99a60)}
.tone-barrage{background:linear-gradient(135deg,#2a2a2a,#7a3a9a 45%,#e0c040)}
.tone-loud{background:linear-gradient(#4a4a4a,#c2202a 50%,#1a1a1a)}
.tone-wedding{left:28px;width:128px;border-radius:0;background:radial-gradient(circle at 60% 25%,#e8a040 0,#a4421a 25%,#1a0e10 70%)}
.pager{position:absolute;left:445px;top:867px;display:flex;gap:5px}
.pager span{width:10px;height:10px;border-radius:50%;background:#9a9a9a}
.pager span.is-current{width:14px;height:14px;margin-top:-2px;background:#b8aac8;border:2px solid #c8c8c8}

/* footer band */
.site-footer{position:absolute;left:0;top:917px;width:950px;height:199px;background:var(--purple);color:#fff}
.footer-col{position:absolute;top:38px;font-size:8px;line-height:12px}
.footer-col h3{font-weight:400;font-size:11.5px;text-transform:uppercase;margin-bottom:14px;letter-spacing:-.1px}
.col-news{left:178px;width:180px}
.col-news p{margin-bottom:11px}
.col-news time{display:block}
.col-subscribe{left:380px;width:185px}
.subscribe-form{margin-top:9px;display:flex;width:184px;height:29px;border:1px solid #fff;border-radius:3px;background:#fff}
.subscribe-form span{flex:1;padding-left:9px;line-height:27px;font-style:italic;font-size:7.5px;color:#999;font-family:Arial,sans-serif}
.subscribe-form b{width:30px;background:var(--purple-deep);border:1px solid #fff;border-radius:3px;display:flex;align-items:center;justify-content:center}
.legal-links{margin-top:10px;font-size:7px;font-family:Arial,sans-serif}
.legal-links a{text-decoration:underline}
.col-contact{left:586px;width:200px}
.col-contact a{text-decoration:underline}
.contact-list{list-style:none;margin-top:11px;padding-left:2px}
.contact-list li{margin-bottom:8px}

/* bottom bar */
.social{position:absolute;left:406px;top:1131px;display:flex;gap:5px}
.social span{width:31px;height:31px;border-radius:50%}
.social .s1{background:#2d5b8a}.social .s2{background:#2a86c4}.social .s3{background:#e0473a}.social .s4{background:#e04a8a}
.to-top{position:absolute;left:773px;top:1134px;width:26px;height:28px;background:var(--purple);display:flex;align-items:center;justify-content:center}
.copyright{position:absolute;left:0;top:1172px;width:950px;text-align:center;font-size:7.5px;color:#444}
</style>
</head>
<body>

<header class="site-header">
  <div class="brand"><span class="brand-dot"></span><span class="brand-name">brightnova.com.hk</span></div>
  <nav class="main-nav">
    <a class="is-active" href="#" style="width:53px">Home</a>
    <a href="#" style="width:60px">About Us</a>
    <a href="#" style="width:59px">Products</a>
    <a href="#" style="width:66px">Events</a>
    <a href="#" style="width:49px">Gallery</a>
    <a href="#" style="width:56px">Contact Us</a>
  </nav>
</header>

<section class="hero" role="img" aria-label="Fireworks bursting over a bay at night with a lit resort on the shore">
  <span class="hero-arrow prev"><svg width="10" height="14" viewBox="0 0 10 14"><path d="M8 1 2 7l6 6" fill="none" stroke="#222" stroke-width="1.5"/></svg></span>
  <span class="hero-arrow next"><svg width="10" height="14" viewBox="0 0 10 14"><path d="M2 1l6 6-6 6" fill="none" stroke="#222" stroke-width="1.5"/></svg></span>
  <p class="hero-caption">Donec ullamcorper nulla non metus auctor fringilla</p>
</section>

<h2 class="section-title welcome-title">Welcome!</h2>
<div class="welcome-photo" role="img" aria-label="White and pink firework burst against a night sky"></div>
<p class="welcome-text">Donec ullamcorper nulla non metus auctor fringilla. Cras justo odio, dapibus ac facilisis in, egestas eget quam. Donec ullamcorper nulla non metus auctor fringilla. Curabitur blandit tempus porttitor. Cras mattis consectetur purus sit amet fermentum. Nullam id dolor id nibh ultricies vehicula ut id elit. Morbi leo risus, porta ac consectetur ac, vestibulum at eros. Aenean lacinia bibendum nulla sed consectetur. Donec ullamcorper nulla non metus auctor fringilla. Cras justo odio, dapibus ac facilisis in, egestas eget quam. Donec ullamcorper nulla non metus auctor fringilla. Curabitur blandit tempus porttitor. Cras mattis consectetur purus sit amet fermentum. Nullam id dolor id nibh ultricies vehicula ut id elit. Morbi leo risus, porta ac consectetur ac, vestibulum at eros. Aenean lacinia bibendum nulla sed consectetur. Donec ullamcorper nulla non metus auctor fringilla. Cras justo odio, dapibus ac facilisis in, egestas eget quam. Donec ullamcorper nulla non metus auctor fringilla.</p>

<h2 class="section-title products-title">Fire Works</h2>
<div class="product-grid">
  <article class="product-card"><div class="product-photo tone-fountain" role="img" aria-label="Row of colourful cone fountains"></div><h4 class="product-label">Fountains</h4></article>
  <article class="product-card"><div class="product-photo tone-kit" role="img" aria-label="Assorted display kit of fireworks"></div><h4 class="product-label">Display Kits</h4></article>
  <article class="product-card"><div class="product-photo tone-rocket" role="img" aria-label="Four silver rockets on sticks"></div><h4 class="product-label">Rockets</h4></article>
  <article class="product-card"><div class="product-photo tone-barrage" role="img" aria-label="Boxed barrage cake"></div><h4 class="product-label">Pro Barrages</h4></article>
  <article class="product-card"><div class="product-photo tone-loud" role="img" aria-label="Red and black firework cake box"></div><h4 class="product-label">You Like it LOUD!!</h4></article>
  <article class="product-card"><div class="product-photo tone-wedding" role="img" aria-label="Wedding couple watching fireworks at night"></div><h4 class="product-label">Wedding Fireworks</h4></article>
</div>
<div class="pager"><span class="is-current"></span><span></span><span></span><span></span></div>

<footer class="site-footer">
  <div class="footer-col col-news">
    <h3>News &amp; Events</h3>
    <p>Phasellus euismod luctus augue at pellentesque. Curabitur rutrum vehicula est at dignissim.<time>3 days ago</time></p>
    <p>Phasellus euismod luctus augue at pellentesque.<time>6 days ago</time></p>
    <p>Phasellus euismod luctus augue at pellentesque.<time>10 days ago</time></p>
  </div>
  <div class="footer-col col-subscribe">
    <h3>Subscribe to our newsletter</h3>
    <p>Enter your email address below to subscribe. You will receive our newsletter once a week.</p>
    <div class="subscribe-form"><span>enter your email address</span><b><svg width="6" height="8" viewBox="0 0 6 8"><path d="M1 1l3 3-3 3" fill="none" stroke="#fff" stroke-width="1.6"/></svg></b></div>
    <p class="legal-links"><a href="#">Terms of Use</a> &nbsp;|&nbsp; <a href="#">Privacy Policy</a></p>
  </div>
  <div class="footer-col col-contact">
    <h3>Let’s keep in touch</h3>
    <p>You can contact us by using the contact information below or by sending us a message via <a href="#">our contact form</a>.</p>
    <ul class="contact-list">
      <li>Street Name, Adress,</li>
      <li>Phone: +1 (310) 555 0148</li>
      <li>Email: info@brightnova.com.hk</li>
    </ul>
  </div>
</footer>

<div class="social" aria-label="Social links"><span class="s1"></span><span class="s2"></span><span class="s3"></span><span class="s4"></span></div>
<a class="to-top" href="#" aria-label="Back to top"><svg width="12" height="8" viewBox="0 0 12 8"><path d="M1 7l5-5 5 5" fill="none" stroke="#fff" stroke-width="1.6"/></svg></a>
<p class="copyright">Brightnova © Copy right 2014 | All rights reserved &nbsp;| &nbsp;Privacy Policy</p>

</body>
</html>
```